Invitation Design Project

50th Birthday Party for Tim. Big, loud party planned with loads of friends and family. at our home. Decorations will be coloured lanterns attached to the pergola and hired a band.

Details:

on 19th October, 2013
(other details when design chosen)
at: 7.00 pm
RSVP: 14th October, 2013

```html
<!DOCTYPE html>
<html lang="en">
<head>
<meta charset="utf-8">
<title>Tim's 50th Birthday Party Invitation</title>
<link rel="stylesheet" href="https://fonts.googleapis.com/css2?family=Cinzel:wght@400;600&family=Montserrat:wght@300;600&display=swap">
<style>
  :root {
    --backdrop: #e9e6e1;
    --ink: #111111;
    --ink-soft: #2a2422;
    --mosaic-red: #9a3a3e;
    --mosaic-rust: #a4573f;
    --mosaic-olive: #7f7f44;
    --mosaic-teal: #3f6f66;
    --mosaic-green: #4f7a46;
    --mosaic-slate: #56585a;
    --mosaic-rose: #b45457;
    --lantern-lime: #d8e27a;
    --lantern-aqua: #a9d6d4;
    --lantern-pink: #f0b3b0;
    --flower-white: #f3efe8;
  }
  * { margin: 0; padding: 0; box-sizing: border-box; }
  html, body {
    width: 1200px;
    height: 1000px;
    overflow: hidden;
    background: var(--backdrop);
  }
  .canvas {
    position: relative;
    width: 1200px;
    height: 1000px;
  }
  .invitation {
    position: absolute;
    left: 314px;
    top: 95px;
    width: 572px;
    height: 810px;
    overflow: hidden;
    box-shadow: 0 6px 24px rgba(0,0,0,0.25);
  }
  .mosaic {
    position: absolute;
    inset: 0;
    background:
      radial-gradient(ellipse at 20% 15%, rgba(63,111,102,0.85), transparent 55%),
      radial-gradient(ellipse at 80% 30%, rgba(63,111,102,0.7), transparent 50%),
      radial-gradient(ellipse at 40% 55%, rgba(127,127,68,0.85), transparent 50%),
      radial-gradient(ellipse at 15% 75%, rgba(164,87,63,0.8), transparent 50%),
      radial-gradient(ellipse at 75% 85%, rgba(180,84,87,0.85), transparent 50%),
      linear-gradient(180deg, var(--mosaic-slate) 0%, var(--mosaic-green) 40%, var(--mosaic-olive) 60%, var(--mosaic-red) 85%, var(--mosaic-rose) 100%);
  }
  .lanterns-left {
    position: absolute;
    left: 0;
    top: 0;
    width: 250px;
    height: 330px;
    border-bottom-right-radius: 120px;
    background: linear-gradient(160deg, rgba(243,239,232,0.55) 0%, rgba(216,226,122,0.55) 40%, rgba(169,214,212,0.5) 65%, rgba(240,179,176,0.5) 100%);
  }
  .lanterns-right {
    position: absolute;
    right: 0;
    top: 0;
    width: 140px;
    height: 175px;
    border-bottom-left-radius: 80px;
    background: linear-gradient(200deg, rgba(243,239,232,0.55) 0%, rgba(154,58,62,0.5) 45%, rgba(216,226,122,0.6) 100%);
  }
  .text {
    position: absolute;
    left: 0;
    width: 100%;
    text-align: center;
    color: var(--ink);
    line-height: 1;
    white-space: nowrap;
  }
  .invited {
    top: 186px;
    font-family: "Cinzel", serif;
    font-size: 22px;
    letter-spacing: 0.5px;
  }
  .headline {
    top: 248px;
    font-family: "Montserrat", sans-serif;
    font-weight: 600;
    font-size: 64px;
    letter-spacing: -0.5px;
  }
  .subhead {
    top: 322px;
    font-family: "Montserrat", sans-serif;
    font-weight: 300;
    font-size: 56px;
    letter-spacing: -0.5px;
  }
  .when {
    font-family: "Cinzel", serif;
    font-weight: 600;
    font-size: 22px;
    color: var(--ink-soft);
  }
  .when-date { top: 413px; }
  .when-time { top: 442px; }
  .rsvp {
    top: 752px;
    font-family: "Cinzel", serif;
    font-size: 21px;
    color: rgba(20,16,16,0.7);
  }
</style>
</head>
<body>
  <main class="canvas">
    <article class="invitation">
      <div class="mosaic" role="img" aria-label="Background of multicoloured triangle mosaic in muted reds, greens and olives"></div>
      <div class="lanterns-left" role="img" aria-label="Illustration of hanging paper lanterns in lime, aqua and pink with white flowers"></div>
      <div class="lanterns-right" role="img" aria-label="Illustration of white floral swirls and a lime flower"></div>

      <p class="text invited">You’re invited</p>
      <h1 class="text headline">Tim’s 50th</h1>
      <h2 class="text subhead">Birthday Party</h2>
      <p class="text when when-date">on 19th October, 2013</p>
      <p class="text when when-time">at: 7.00 pm</p>
      <p class="text rsvp">RSVP: 14th October, 2013</p>
    </article>
  </main>
</body>
</html>
```